Redesign website for small print company

Vindaborgprent is a small printing company in Iceland mainly servicing Students, schools, etc. We are also doing all kind of other jobs, like business cards, book printing, brochure printing etc. We are also selling books online.
Our website is: www.vindaborgprent.is
What we are looking for is:
- Web Design (Uncoded - PSD layout only)
- Mobile friendly design, using our current color scheme: Red, green, yellow and light gray.
- Clean simple design
- Simple, light and easy to use.
- More menu Items/drop down
Industry/Entity Type
Digital Printing
Number of Pages Required
5+ page
Requirements
Must have
- Easy navigation
- Designed for mobile
- Current color scheme (see logo)
Nice to have
- Icon based products

```html
<!DOCTYPE html>
<html lang="en">
<head>
<meta charset="utf-8">
<title>Vindaborgprent</title>
<link href="https://fonts.googleapis.com/css2?family=Roboto+Condensed:wght@400;500;700&family=Roboto:wght@400;500&family=Mulish:wght@400;500&display=swap" rel="stylesheet">
<style>
:root{
  --red:#ef3a32;
  --yellow:#f6cf00;
  --ink:#2f2f2f;
  --text:#333;
  --line:#e3e3e3;
  --icon:#c9c9c9;
  --white:#fff;
}
*{margin:0;padding:0;box-sizing:border-box}
html,body{width:1200px;height:898px;overflow:hidden;background:var(--white)}
body{font-family:"Mulish",sans-serif;color:var(--text);position:relative}
.topbar{height:32px;border-bottom:1px solid var(--line);position:relative}
.topbar .contact{position:absolute;left:135px;top:8px;font:400 12.5px "Roboto",sans-serif;color:var(--ink)}
.account{position:absolute;right:136px;top:0;height:32px;display:flex}
.account a{display:flex;align-items:center;gap:6px;font:500 12.5px "Roboto",sans-serif;color:var(--ink);text-decoration:none;padding:0 13px}
.account a+a{border-left:1px solid var(--line);border-right:1px solid var(--line)}
.header{height:73px;position:relative}
.brand{position:absolute;left:135px;top:15px;display:flex;align-items:center;gap:6px;font:700 26px "Roboto Condensed",sans-serif;color:var(--ink);letter-spacing:.3px}
.brand .mark{width:30px;height:39px;background:var(--red)}
.nav{position:absolute;left:572px;top:28px;display:flex;gap:20px;font:500 14.6px "Roboto",sans-serif;color:var(--ink)}
.nav span{position:relative;white-space:nowrap}
.nav .drop::after{content:"";position:absolute;left:50%;top:22px;width:6px;height:6px;border-right:1.5px solid var(--ink);border-bottom:1.5px solid var(--ink);transform:translateX(-50%) rotate(45deg)}
.cart{position:absolute;left:922px;top:16px;width:142px;height:38px;border-radius:19px;background:var(--red);color:var(--white);display:flex;align-items:center;padding-left:24px;gap:8px;font:500 15px "Roboto",sans-serif}
.cart .count{position:absolute;left:-8px;top:6px;width:27px;height:27px;border-radius:50%;background:var(--yellow);font-size:13px;display:flex;align-items:center;justify-content:center}
.hero{position:absolute;left:0;top:105px;width:1200px;height:466px;background:radial-gradient(ellipse at 60% 40%,#4a413a,#2e2925 70%);text-align:center;color:var(--white)}
.hero h1{margin-top:212px;font:700 45px "Roboto Condensed",sans-serif;letter-spacing:.2px}
.hero h1 em{font-style:normal;color:var(--red)}
.hero p{margin:18px auto 0;width:680px;font:400 22px/30px "Mulish",sans-serif}
.categories{position:absolute;top:428px;left:0;width:1200px;display:flex;justify-content:center;gap:33px;font:400 16px "Mulish",sans-serif}
.features{position:absolute;top:571px;left:0;width:1200px;text-align:center}
.features h2{margin-top:44px;font:700 36px "Roboto Condensed",sans-serif;color:var(--ink)}
.features .lead{margin-top:8px;font:400 15px/24px "Mulish",sans-serif;color:var(--text)}
.grid{position:absolute;left:135px;top:178px;width:930px;display:flex}
.item{flex:1;height:130px;border-left:1px solid var(--line);padding-top:10px}
.item:first-child{border-left:none}
.item svg{height:30px}
.item h3{margin-top:6px;font:500 20px "Roboto Condensed",sans-serif;color:var(--ink)}
.item p{margin-top:7px;font:400 12px/18px "Mulish",sans-serif;color:var(--text)}
</style>
</head>
<body>
<div class="topbar">
  <div class="contact">Tel: 555 0142 | verk@vindaborgprent.is | Mon - Fri: 9-17</div>
  <div class="account">
    <a href="#"><svg width="16" height="16" viewBox="0 0 16 16" fill="none" stroke="#333" stroke-width="1.3"><rect x="2" y="7" width="12" height="8"/><path d="M5 7V4.5a3 3 0 0 1 6 0V7"/><circle cx="8" cy="11" r="1"/></svg>Login</a>
    <a href="#"><svg width="16" height="16" viewBox="0 0 16 16" fill="none" stroke="#333" stroke-width="1.3"><circle cx="8" cy="5" r="3.5"/><path d="M1 15.5c1-4 3.5-5.5 7-5.5s6 1.5 7 5.5z"/></svg>Sign up</a>
  </div>
</div>
<header class="header">
  <div class="brand"><span class="mark"></span>VINDABORGPRENT</div>
  <nav class="nav"><span>HOME</span><span class="drop">SERVICES</span><span>JOB SUBMIT</span><span>ABOUT US</span></nav>
  <div class="cart"><span class="count">05</span>
    <svg width="18" height="16" viewBox="0 0 18 16" fill="#fff"><path d="M0 5h18v2h-1l-2 8H3L1 7H0z"/><path d="M5 5l3-5M13 5l-3-5" stroke="#fff" stroke-width="1.5"/></svg>
    700.00kr
    <svg width="12" height="8" viewBox="0 0 12 8" fill="none" stroke="#fff" stroke-width="1.6"><path d="M1 1l5 5 5-5"/></svg>
  </div>
</header>
<section class="hero" role="img" aria-label="Dimmed desk top with laptop, coffee cup, notebooks and newspapers">
  <h1>WELCOME TO <em>UNIVERSITY</em></h1>
  <p>Specialized in the service of school staff, as well as providing general public printing.</p>
  <div class="categories"><span>Essays</span><span>Business Cards</span><span>leafleats</span><span>Poster</span><span>Book Printing</span><span>Brochure Printing</span><span>Textbooks</span></div>
</section>
<section class="features">
  <h2>FEATURES &amp; BENEFITS</h2>
  <p class="lead">This is Draftwell's version &nbsp;of Lorem Ipsum. Proin gravida nibh vel velit auctor aliquet.<br>Aenean sollicitudin, lorem quis bibendum auctor</p>
  <div class="grid">
    <div class="item">
      <svg viewBox="0 0 32 30" width="32" fill="var(--icon)"><rect x="12" y="3" width="8" height="5"/><rect x="4" y="10" width="24" height="4"/><rect x="8" y="16" width="16" height="4"/><rect x="2" y="22" width="28" height="5"/></svg>
      <h3>Flexibility</h3>
      <p>This is Draftwell's version &nbsp;of Lorem<br>Ipsum. Proin gravida nibh.</p>
    </div>
    <div class="item">
      <svg viewBox="0 0 30 30" width="30" fill="none" stroke="var(--icon)" stroke-width="3"><circle cx="15" cy="15" r="12.5"/><path d="M15 8v8h-5"/></svg>
      <h3>On Time Delivery</h3>
      <p>This is Draftwell's version &nbsp;of Lorem<br>Ipsum. Proin gravida nibh.</p>
    </div>
    <div class="item">
      <svg viewBox="0 0 32 30" width="32" fill="var(--icon)"><rect x="2" y="1" width="3" height="29"/><path d="M6 3c6-3 10 3 16 1 3-1 6-2 8-2v15c-4 0-6 3-11 2-5-1-8-4-13-1z"/></svg>
      <h3>Freedom</h3>
      <p>This is Draftwell's version &nbsp;of Lorem<br>Ipsum. Proin gravida nibh.</p>
    </div>
    <div class="item">
      <svg viewBox="0 0 26 30" width="26" fill="var(--icon)"><path d="M5 13V9a8 8 0 0 1 16 0v4h-4V9a4 4 0 0 0-8 0v4z"/><rect x="1" y="13" width="24" height="17" rx="1"/></svg>
      <h3>Customers trust us</h3>
      <p>This is Draftwell's version &nbsp;of Lorem<br>Ipsum. Proin gravida nibh.</p>
    </div>
  </div>
</section>
</body>
</html>
```